Online business manager needs a website

I need a website designed and then coded. I am an online business manager serving a number of different industries providing administrative support to existing small businesses and helping solo practitioners get their new business up and running.

I didn't have a logo formally designed but have been using the attached avatar and wouldn't mind something that incorporated that.

The business doesn't have an official name, so I've just been using my name Lena Pruvost, Online Business Manager or Lena Pruvost, OBM. I've attached two documents that I have made previously for an example of content.

I would prefer the final site be in Wordpress.

Requirements
Must have
• A way to contact me, testimonials, list of services

```html
<!DOCTYPE html>
<html lang="en">
<head>
<meta charset="utf-8">
<title>Lena Pruvost — Virtual Assistant</title>
<link href="https://fonts.googleapis.com/css2?family=Poppins:wght@300;400;500;600&family=Great+Vibes&display=swap" rel="stylesheet">
<style>
:root{
  --purple:#6a3d9a;
  --purple-soft:#8a5cc0;
  --dark:#2b2522;
  --ink:#2a2a33;
  --muted:#6c6c78;
  --bg-soft:#f4f4f8;
  --white:#ffffff;
  --orange:#f7931e;
  --red:#f15a29;
  --green:#7dc242;
  --blue:#29abe2;
  --line:#e6e6ee;
}
*{box-sizing:border-box;margin:0;padding:0}
html,body{width:1200px;height:3626px;overflow:hidden}
body{position:relative;font-family:"Poppins",sans-serif;color:var(--ink);background:var(--white)}
.abs{position:absolute}
.script{font-family:"Great Vibes",cursive;color:var(--purple);font-weight:400}

/* header + dark panel */
.dark-panel{left:0;top:0;width:652px;height:1320px;background:var(--dark);border-bottom-right-radius:4px}
.logo{left:110px;top:22px;color:var(--white)}
.logo-name{font-size:22px;font-weight:500;letter-spacing:1px;line-height:1}
.logo-tag{font-family:"Great Vibes",cursive;font-size:19px;margin-left:54px;line-height:1}
.nav{left:332px;top:38px;display:flex;gap:24px;font-size:15px;color:var(--white)}
.top-phone{left:793px;top:38px;font-size:14px;color:var(--ink);display:flex;align-items:center;gap:5px}
.btn{display:inline-flex;align-items:center;gap:10px;border-radius:22px;font-size:16px;font-weight:400}
.btn-contact{left:942px;top:25px;width:142px;height:40px;background:var(--purple);color:var(--white);justify-content:center}

.hero{left:109px;top:94px;width:982px;height:554px;background:var(--purple);border-radius:28px;overflow:hidden}
.hero-photo{left:0;top:0;width:430px;height:468px;background:linear-gradient(140deg,#b08a6a,#d9a987 45%,#6f6f75);border-radius:0 60% 55% 40% / 0 48% 52% 40%}
.hero-streak{background:rgba(255,255,255,.12);border-radius:30px;transform:rotate(-50deg)}
.hero h1{left:555px;top:110px;width:400px;font-size:43px;line-height:52px;font-weight:600;color:var(--white)}
.hero p{left:555px;top:292px;width:340px;font-size:16px;line-height:28px;color:var(--white);font-weight:300}
.btn-services{left:555px;top:382px;width:156px;height:44px;background:var(--white);color:var(--purple);justify-content:center}
.dot{border-radius:50%}

.help-kicker{left:124px;top:748px;font-size:36px}
.help-title{left:124px;top:810px;width:420px;font-size:28px;line-height:44px;font-weight:500;color:var(--white)}
.help-rule{left:121px;top:924px;width:428px;height:1px;background:#55504d}
.help-lead{left:124px;top:956px;width:420px;font-size:17px;line-height:28px;color:var(--purple-soft)}
.help-body{left:124px;top:1028px;width:408px;font-size:14.5px;line-height:27px;color:#e6e3e0;font-weight:300}
.btn-all{left:124px;top:1171px;width:176px;height:47px;background:var(--purple);color:var(--white);justify-content:center}

.card{width:236px;height:222px;background:var(--white);border:1px solid var(--line);border-radius:22px 22px 22px 22px;text-align:center;box-shadow:0 6px 20px rgba(0,0,0,.04)}
.card.active{border:2px solid var(--purple)}
.card svg.icon{margin-top:36px}
.card-title{font-size:17px;line-height:22px;margin-top:10px;color:#3a3a44}
.card-arrow{position:absolute;right:26px;bottom:24px;width:34px;height:34px;border-radius:50%;border:1px solid #bbb;display:flex;align-items:center;justify-content:center}
.card.active .card-arrow{background:var(--purple);border-color:var(--purple)}

/* about */
.about-bg{left:0;top:1320px;width:1200px;height:760px;background:var(--bg-soft)}
.about-photo{left:224px;top:1551px;width:292px;height:292px;border-radius:50%;background:radial-gradient(circle at 50% 60%,#e9d8cf 0 30%,#c0307a 55%,#6b2a4a)}
.about-title{left:662px;top:1462px;font-size:60px}
.about-sub{left:664px;top:1554px;width:400px;font-size:22px;line-height:32px;font-weight:400}
.about-text{left:664px;top:1630px;width:400px;font-size:14.5px;line-height:27px;color:var(--muted);font-weight:300}
.sec-title{font-size:60px}

/* portfolio */
.tile{border:2px solid #d5d0e0}

/* testimonials */
.testi-card{left:214px;top:2883px;width:772px;height:290px;background:var(--white);border-radius:40px;box-shadow:0 10px 40px rgba(0,0,0,.06);text-align:center}
.testi-card p{width:680px;margin:126px auto 0;font-size:14.5px;line-height:27px;color:var(--muted);font-weight:300}
.testi-author{margin-top:18px;font-size:14px}
.testi-author b{font-weight:500;color:var(--ink)}
.testi-author span{color:var(--muted)}
.avatar{border-radius:50%;background:linear-gradient(150deg,#d9c3b3,#a98f82)}

/* footer */
.footer-logo{left:150px;top:3440px;color:var(--purple)}
.footer h4{font-size:14px;font-weight:400;line-height:21px}
.flinks{list-style:none;font-size:13.5px;line-height:22.5px;color:var(--purple)}
.flinks li::before{content:"–  ";color:#999}
.social{width:30px;height:30px;border-radius:50%;background:var(--purple)}
</style>
</head>
<body>

<div class="abs dark-panel"></div>

<header>
  <div class="abs logo">
    <div class="logo-name">Lena Pruvost</div>
    <div class="logo-tag">Virtual Assistant</div>
  </div>
  <nav class="abs nav"><span>Home</span><span>About</span><span>Services</span><span>Portfolio</span></nav>
  <div class="abs top-phone">
    <svg width="13" height="13" viewBox="0 0 24 24"><path fill="#444" d="M6.6 10.8a15 15 0 0 0 6.6 6.6l2.2-2.2c.3-.3.7-.4 1-.2 1.1.4 2.3.6 3.6.6.6 0 1 .4 1 1V20c0 .6-.4 1-1 1A17 17 0 0 1 3 4c0-.6.4-1 1-1h3.5c.6 0 1 .4 1 1 0 1.3.2 2.5.6 3.6.1.3 0 .7-.2 1z"/></svg>
    555.014.2290
  </div>
  <a class="abs btn btn-contact">
    <svg width="18" height="18" viewBox="0 0 20 20"><circle cx="10" cy="10" r="8.5" fill="none" stroke="#fff" stroke-width="1.4"/><path d="M6 10h8M11 7l3 3-3 3" fill="none" stroke="#fff" stroke-width="1.4"/></svg>
    Contact
  </a>
</header>

<section class="abs hero">
  <div class="abs hero-streak" style="left:300px;top:-20px;width:60px;height:230px"></div>
  <div class="abs hero-streak" style="left:230px;top:300px;width:50px;height:230px"></div>
  <div class="abs hero-photo" role="img" aria-label="Portrait photo of Lena smiling outdoors"></div>
  <div class="abs dot" style="left:494px;top:148px;width:14px;height:14px;background:var(--green)"></div>
  <div class="abs dot" style="left:465px;top:422px;width:18px;height:18px;background:var(--orange)"></div>
  <div class="abs dot" style="left:867px;top:422px;width:18px;height:18px;background:var(--red)"></div>
  <div class="abs dot" style="left:66px;top:472px;width:18px;height:18px;background:var(--blue)"></div>
  <h1 class="abs">Helping Business Achieve Their Goals.</h1>
  <p class="abs">A business strategy is the means by which it sets out to achieve its desired ends.</p>
  <a class="abs btn btn-services">
    <svg width="18" height="18" viewBox="0 0 20 20"><circle cx="10" cy="10" r="8.5" fill="none" stroke="#6a3d9a" stroke-width="1.4"/><path d="M6 10h8M11 7l3 3-3 3" fill="none" stroke="#6a3d9a" stroke-width="1.4"/></svg>
    Services
  </a>
</section>

<section class="services">
  <div class="abs script help-kicker">How we help.</div>
  <h2 class="abs help-title">We help to stay connected with your audience</h2>
  <div class="abs help-rule"></div>
  <p class="abs help-lead">We have the best experts to elevate your business to the next level, try is and you will see!</p>
  <p class="abs help-body">Lorem Ipsum is simply dummy text of the printing and typesetting industry. Lorem Ipsum has been the industry's standard dummy text ever since the 1500s, when an unknown printer took a galley of type and.</p>
  <a class="abs btn btn-all">All Services
    <svg width="14" height="14" viewBox="0 0 14 14"><path d="M3 11L11 3M5 3h6v6" fill="none" stroke="#fff" stroke-width="1.6"/></svg>
  </a>

  <div class="abs card active" style="left:600px;top:741px">
    <svg class="icon" width="56" height="56" viewBox="0 0 56 56" fill="none" stroke="#555" stroke-width="1.6"><rect x="14" y="8" width="34" height="24" rx="2"/><path d="M20 28v-6M26 28V16M32 28v-9M38 28V12" stroke="#6a3d9a"/><circle cx="14" cy="34" r="5"/><path d="M4 52c0-7 4-11 10-11s10 4 10 11M24 46h22"/></svg>
    <div class="card-title">Virtual<br>Assistance</div>
    <div class="card-arrow"><svg width="12" height="12" viewBox="0 0 12 12"><path d="M3 9L9 3M4 3h5v5" fill="none" stroke="#fff" stroke-width="1.5"/></svg></div>
  </div>
  <div class="abs card" style="left:857px;top:741px">
    <svg class="icon" width="56" height="56" viewBox="0 0 56 56" fill="none" stroke="#555" stroke-width="1.6"><rect x="6" y="8" width="40" height="30" rx="2"/><path d="M20 38l-3 8h22l-3-8M12 15h12v9H12zM28 15h12M28 20h10M12 29h28"/><path d="M36 26L50 6l3 3-14 20-5 2z" stroke="#6a3d9a"/></svg>
    <div class="card-title">Content<br>Management</div>
    <div class="card-arrow"><svg width="12" height="12" viewBox="0 0 12 12"><path d="M2 6h8M7 3l3 3-3 3" fill="none" stroke="#777" stroke-width="1.3"/></svg></div>
  </div>
  <div class="abs card" style="left:600px;top:985px">
    <svg class="icon" width="56" height="56" viewBox="0 0 56 56" fill="none" stroke="#555" stroke-width="1.6"><circle cx="16" cy="38" r="12"/><path d="M19 33c-1-2-6-2-6 1s6 2 6 5-5 3-6 1M16 30v16" stroke="#6a3d9a"/><path d="M32 50V36M38 50V30M44 50V24M50 50V18M30 24l8-10 6 5 8-12"/></svg>
    <div class="card-title">Finance<br>Management</div>
    <div class="card-arrow"><svg width="12" height="12" viewBox="0 0 12 12"><path d="M2 6h8M7 3l3 3-3 3" fill="none" stroke="#777" stroke-width="1.3"/></svg></div>
  </div>
  <div class="abs card" style="left:857px;top:985px">
    <svg class="icon" width="56" height="56" viewBox="0 0 56 56" fill="none" stroke="#555" stroke-width="1.6"><circle cx="14" cy="10" r="5"/><path d="M6 30c0-8 3-12 8-12s8 4 8 12M10 30v20M18 30v20"/><circle cx="40" cy="30" r="7" stroke="#6a3d9a"/><circle cx="40" cy="30" r="2.5" stroke="#6a3d9a"/><rect x="28" y="6" width="20" height="12" rx="2"/></svg>
    <div class="card-title">Business<br>Management</div>
    <div class="card-arrow"><svg width="12" height="12" viewBox="0 0 12 12"><path d="M2 6h8M7 3l3 3-3 3" fill="none" stroke="#777" stroke-width="1.3"/></svg></div>
  </div>
</section>

<section class="about">
  <div class="abs about-bg"></div>
  <svg class="abs" style="left:1154px;top:1610px" width="46" height="92" viewBox="0 0 46 92"><path d="M46 0v92C20 92 0 72 0 46S20 0 46 0z" fill="#6a3d9a"/></svg>
  <div class="abs dot" style="left:468px;top:1572px;width:128px;height:128px;background:var(--purple)"></div>
  <div class="abs dot" style="left:134px;top:1728px;width:102px;height:102px;background:var(--purple)"></div>
  <div class="abs dot" style="left:170px;top:1524px;width:20px;height:20px;background:var(--orange)"></div>
  <div class="abs dot" style="left:449px;top:1527px;width:20px;height:20px;border:1.5px solid var(--blue)"></div>
  <div class="abs dot" style="left:525px;top:1760px;width:13px;height:13px;background:#1a9b5c"></div>
  <div class="abs about-photo" role="img" aria-label="Portrait photo of Lena in front of flowering shrubs"></div>
  <h2 class="abs script about-title">About Me</h2>
  <svg class="abs" style="left:874px;top:1488px" width="116" height="36" viewBox="0 0 116 36"><path d="M2 4c0 20 14 34 44 22S96 8 110 14" fill="none" stroke="#6a3d9a" stroke-width="1.4" stroke-dasharray="4 4"/><path d="M104 9l7 5-7 4" fill="none" stroke="#6a3d9a" stroke-width="1.4"/></svg>
  <p class="abs about-sub">Hi! I'm so excited that you have chosen to explore my portfolio.</p>
  <p class="abs about-text">Helping businesses achieve their goals is my passion, and I'm thrilled that with my assistance you will have more time for your own passion project. I thrive while working independently, which means you can be confident when leaving tasks for me. The type of work that lights me up is anything involving organization and/or spreadsheets. You need data analyzed that includes multiple nested if formulas? You have an overwhelming amount of email to sort through and appointments to book? I'm your gal!</p>
</section>

<section class="portfolio">
  <h2 class="abs script sec-title" style="left:448px;top:2004px">Portfolio</h2>
  <svg class="abs" style="left:636px;top:2028px" width="116" height="36" viewBox="0 0 116 36"><path d="M2 4c0 20 14 34 44 22S96 8 110 14" fill="none" stroke="#6a3d9a" stroke-width="1.4" stroke-dasharray="4 4"/><path d="M104 9l7 5-7 4" fill="none" stroke="#6a3d9a" stroke-width="1.4"/></svg>

  <div class="abs tile" style="left:160px;top:2115px;width:436px;height:258px;background:linear-gradient(135deg,#f3d6dc,#e9c7cf)" role="img" aria-label="Podcast episode cover with headphones and keyboard on a pink desk"></div>
  <div class="abs tile" style="left:604px;top:2115px;width:436px;height:168px;background:linear-gradient(90deg,#8d6fbe,#6d4fa4 70%,#5a3f95)" role="img" aria-label="Pet adoption social graphic with a purple overlay">
    <div style="position:absolute;left:0;right:0;top:46px;text-align:center;color:#fff;font-size:20px;font-weight:500">
      <svg width="30" height="30" viewBox="0 0 30 30" style="display:block;margin:0 auto 8px"><circle cx="12" cy="12" r="8" fill="none" stroke="#fff" stroke-width="2.4"/><path d="M18 18l8 8" stroke="#fff" stroke-width="2.8"/></svg>
      View More
    </div>
  </div>
  <div class="abs tile" style="left:604px;top:2290px;width:214px;height:330px;background:linear-gradient(180deg,#fb8b45 0 58%,#d8d2cc 58%)" role="img" aria-label="Graphic with tips for looking great on video calls"></div>
  <div class="abs tile" style="left:827px;top:2290px;width:213px;height:160px;background:linear-gradient(135deg,#fbe3dc,#f5cfc3)" role="img" aria-label="Podcast guest promotion graphic"></div>
  <div class="abs tile" style="left:827px;top:2458px;width:213px;height:162px;background:linear-gradient(90deg,#2a0c22,#5c1747 50%,#2a0c22)" role="img" aria-label="Audio waveform graphic in pink on dark background"></div>
  <div class="abs tile" style="left:160px;top:2380px;width:215px;height:240px;background:#f85a5a" role="img" aria-label="Quote graphic in red"></div>
  <div class="abs tile" style="left:382px;top:2380px;width:214px;height:240px;background:linear-gradient(135deg,#faf6f1,#eadfd5)" role="img" aria-label="Podcast episode graphic with guest portrait"></div>
</section>

<section class="testimonials">
  <h2 class="abs script sec-title" style="left:412px;top:2782px">Testimonials</h2>
  <svg class="abs" style="left:672px;top:2806px" width="116" height="36" viewBox="0 0 116 36"><path d="M2 4c0 20 14 34 44 22S96 8 110 14" fill="none" stroke="#6a3d9a" stroke-width="1.4" stroke-dasharray="4 4"/><path d="M104 9l7 5-7 4" fill="none" stroke="#6a3d9a" stroke-width="1.4"/></svg>

  <div class="abs avatar" style="left:45px;top:2868px;width:86px;height:86px" role="img" aria-label="Client photo"></div>
  <div class="abs avatar" style="left:147px;top:3000px;width:76px;height:76px" role="img" aria-label="Client photo"></div>
  <div class="abs avatar" style="left:-2px;top:3116px;width:62px;height:86px;border-radius:0 50% 50% 0" role="img" aria-label="Client photo"></div>
  <div class="abs avatar" style="left:962px;top:2923px;width:86px;height:86px;background:linear-gradient(150deg,#bfe3ef,#8ccbe0)" role="img" aria-label="Client photo"></div>
  <div class="abs avatar" style="left:1098px;top:3047px;width:88px;height:88px" role="img" aria-label="Client photo"></div>

  <div class="abs testi-card">
    <div class="abs avatar" style="left:346px;top:32px;width:80px;height:80px;background:linear-gradient(150deg,#e4a56b,#9c6a4e)" role="img" aria-label="Photo of Dana R."></div>
    <p>When it became apparent that a project would take more time than I had, Lena stepped up to take on the required research. She was thorough and timely; able to meet a last-minute 12-hour deadline. I would highly recommend Lena to assist with your next project.</p>
    <div class="testi-author"><b>Dana R.</b> <span>Owner, Northridge Roofing</span></div>
  </div>

  <svg class="abs" style="left:555px;top:3207px" width="92" height="18" viewBox="0 0 92 18">
    <circle cx="7" cy="9" r="6" fill="none" stroke="#aaa"/><circle cx="26" cy="9" r="6" fill="none" stroke="#aaa"/><circle cx="46" cy="9" r="8" fill="#6a3d9a"/><circle cx="66" cy="9" r="6" fill="none" stroke="#aaa"/><circle cx="85" cy="9" r="6" fill="none" stroke="#aaa"/>
  </svg>
</section>

<footer class="footer">
  <div class="abs footer-logo">
    <div class="logo-name" style="font-size:26px">Lena Pruvost</div>
    <div class="logo-tag" style="font-size:22px;margin-left:64px">Virtual Assistant</div>
  </div>
  <h4 class="abs" style="left:436px;top:3403px">Do you have questions?<br>Call o visit us.</h4>
  <div class="abs" style="left:436px;top:3477px;display:flex;align-items:center;gap:14px;font-size:19px">
    <svg width="22" height="22" viewBox="0 0 24 24"><path fill="#9a9aa5" d="M6.6 10.8a15 15 0 0 0 6.6 6.6l2.2-2.2c.3-.3.7-.4 1-.2 1.1.4 2.3.6 3.6.6.6 0 1 .4 1 1V20c0 .6-.4 1-1 1A17 17 0 0 1 3 4c0-.6.4-1 1-1h3.5c.6 0 1 .4 1 1 0 1.3.2 2.5.6 3.6.1.3 0 .7-.2 1z"/></svg>
    555.014.2290
  </div>
  <div class="abs" style="left:436px;top:3538px;display:flex;align-items:center;gap:14px;font-size:14px">
    <svg width="24" height="16" viewBox="0 0 24 16"><rect width="24" height="16" rx="1" fill="#9a9aa5"/><path d="M1 1l11 8 11-8" fill="none" stroke="#fff" stroke-width="1.4"/></svg>
    hello@pruvostobm.com
  </div>
  <h4 class="abs" style="left:741px;top:3403px">Quick Links</h4>
  <ul class="abs flinks" style="left:741px;top:3440px">
    <li>Home</li><li>About Me</li><li>Services</li><li>Testimonials</li><li>Potfolio</li><li>Contact</li>
  </ul>
  <h4 class="abs" style="left:940px;top:3403px">Connect with us</h4>
  <a class="abs social" style="left:943px;top:3450px" aria-label="Social profile one"></a>
  <a class="abs social" style="left:981px;top:3450px" aria-label="Social profile two"></a>
</footer>

</body>
</html>
```